Harmony Four Showcase
Date: Sunday Oct 2, 2022
When: 2-4 p.m.
Location: Brindle9 Alehouse
413 Marigold Wy #200, Sacramento, CA 95821
Tickets: www.Ticketwisp.example
General seating: $15 for adults and $10 for students

```html
<!DOCTYPE html>
<html lang="en">
<head>
<meta charset="utf-8">
<title>Harmony Four Showcase</title>
<link rel="stylesheet" href="https://fonts.googleapis.com/css2?family=Allura&family=Cinzel:wght@400;700;900&family=Cormorant+Garamond:wght@400;500&display=swap">
<style>
  :root {
    --maroon-deep: #1e0003;
    --maroon: #3a0207;
    --crimson: #c41a12;
    --glow: #e2311f;
    --plum: #3b1b3a;
    --leaf-dark: #2a0a10;
    --leaf-mid: #5a1a22;
    --gold-light: #fff4c2;
    --gold: #e0b95a;
    --gold-deep: #9a6a1c;
    --cream: #fbf3e6;
    --ink: #1a0a04;
  }
  html, body {
    margin: 0;
    padding: 0;
    overflow: hidden;
    background: var(--maroon-deep);
  }
  .poster {
    position: relative;
    width: 927px;
    height: 1200px;
    overflow: hidden;
    background:
      radial-gradient(ellipse 420px 360px at 460px 590px, var(--glow) 0%, rgba(196,26,18,0.55) 40%, rgba(58,2,7,0) 80%),
      radial-gradient(ellipse 260px 300px at 640px 520px, rgba(110,70,120,0.35) 0%, rgba(59,27,58,0) 80%),
      linear-gradient(180deg, var(--maroon-deep) 0%, var(--maroon) 28%, #5a0a0e 55%, var(--leaf-dark) 100%);
    color: var(--cream);
    font-family: "Cormorant Garamond", serif;
  }
  .foliage {
    position: absolute;
    left: 0;
    right: 0;
    bottom: 0;
    height: 430px;
    background:
      radial-gradient(ellipse 300px 160px at 180px 330px, rgba(90,26,34,0.8), rgba(42,10,16,0) 80%),
      radial-gradient(ellipse 320px 170px at 760px 360px, rgba(80,30,40,0.8), rgba(42,10,16,0) 80%),
      linear-gradient(180deg, rgba(42,10,16,0) 0%, rgba(60,18,26,0.7) 45%, var(--leaf-dark) 100%);
  }
  .melody-ribbon {
    position: absolute;
    left: 0;
    top: 560px;
    width: 927px;
    height: 232px;
    background: radial-gradient(ellipse 470px 70px at 463px 120px, rgba(224,185,90,0.28), rgba(224,185,90,0) 85%);
  }
  .brand {
    position: absolute;
    top: 40px;
    left: 0;
    width: 100%;
    text-align: center;
    font-size: 64px;
    font-weight: 500;
    color: var(--cream);
    line-height: 1;
  }
  .brand-mark {
    display: inline-block;
    width: 14px;
    height: 14px;
    border-radius: 50%;
    background: var(--cream);
    margin-left: 10px;
    vertical-align: middle;
  }
  .kicker {
    position: absolute;
    top: 156px;
    left: 54px;
    font-family: "Allura", cursive;
    font-size: 68px;
    color: var(--gold);
    line-height: 1;
  }
  .headline {
    position: absolute;
    top: 232px;
    left: 0;
    width: 100%;
    text-align: center;
    font-family: "Cinzel", serif;
    font-weight: 900;
    font-size: 112px;
    letter-spacing: 4px;
    line-height: 1.05;
    background: linear-gradient(180deg, var(--gold-light) 0%, var(--gold) 45%, var(--gold-deep) 70%, var(--gold) 100%);
    -webkit-background-clip: text;
    background-clip: text;
    color: transparent;
    filter: drop-shadow(0 6px 6px rgba(0,0,0,0.7));
  }
  .date {
    position: absolute;
    top: 390px;
    left: 0;
    width: 100%;
    text-align: center;
    font-size: 48px;
    line-height: 1.1;
  }
  .rule {
    position: absolute;
    left: 207px;
    width: 506px;
    height: 1px;
    background: linear-gradient(90deg, rgba(224,185,90,0), var(--gold) 15%, var(--gold) 85%, rgba(224,185,90,0));
  }
  .rule--top { top: 460px; }
  .rule--bottom { top: 525px; }
  .time {
    position: absolute;
    top: 470px;
    left: 0;
    width: 100%;
    text-align: center;
    font-family: "Cinzel", serif;
    font-size: 38px;
    line-height: 1.2;
  }
  .venue {
    position: absolute;
    top: 846px;
    left: 0;
    width: 100%;
    text-align: center;
    font-family: "Cinzel", serif;
    font-size: 42px;
    line-height: 1.2;
  }
  .address {
    position: absolute;
    top: 910px;
    left: 0;
    width: 100%;
    text-align: center;
    font-size: 36px;
    line-height: 1.2;
  }
  .tickets {
    position: absolute;
    top: 1021px;
    left: 216px;
    width: 488px;
    height: 46px;
    border-radius: 23px;
    background: linear-gradient(90deg, var(--gold) 0%, var(--gold-light) 55%, #fbe9a8 100%);
    color: var(--ink);
    font-family: Arial, Helvetica, sans-serif;
    font-weight: 700;
    font-size: 23px;
    line-height: 46px;
    text-align: center;
  }
  .pricing {
    position: absolute;
    top: 1117px;
    left: 0;
    width: 100%;
    text-align: center;
    font-family: Arial, Helvetica, sans-serif;
    font-weight: 700;
    font-size: 24px;
    letter-spacing: 0.2px;
    color: var(--cream);
  }
</style>
</head>
<body>
  <main class="poster">
    <div class="foliage" role="img" aria-label="Dark autumn leaves photograph along the lower edge"></div>
    <div class="melody-ribbon" role="img" aria-label="Glowing golden musical staff with notes sweeping across the poster"></div>

    <div class="brand">Melodin<span class="brand-mark"></span></div>

    <div class="kicker">Harmony Four</div>
    <h1 class="headline" style="margin:0">SHOWCASE</h1>

    <div class="date">Sunday Oct 2, 2022</div>
    <div class="rule rule--top"></div>
    <div class="time">AT 2-4 P.M.</div>
    <div class="rule rule--bottom"></div>

    <div class="venue">BRINDLE9 ALEHOUSE</div>
    <div class="address">413 Marigold Wy #200, Sacramento, CA 95821</div>

    <div class="tickets">Tickets: www.Ticketwisp.example</div>

    <div class="pricing">GENERAL SEATING: $15 FOR ADULTS &nbsp;•&nbsp; $10 FOR STUDENTS</div>
  </main>
</body>
</html>
```